Business cards and stationary for Auto Body Shop
R & T Auto Body Service Inc.
Simple
Delmor Quenivash
28476 Pellway Street
Corvale, CA 91890
rtautobodyinc@brivomail.com
www.rtautobody-example.com
Just the Logo I guess.
Please us this new logo.

```html
<!DOCTYPE html>
<html lang="en">
<head>
<meta charset="utf-8">
<title>R &amp; T Auto Body — Business Cards</title>
<link rel="stylesheet" href="https://fonts.googleapis.com/css2?family=Cinzel:wght@400;600&display=swap">
<style>
  :root {
    --backdrop: #e4e5e7;
    --card: #ffffff;
    --ink: #2e2e30;
    --ink-soft: #5a5a5e;
    --band-dark: #3a3738;
    --band-mid: #8b8889;
    --band-light: #c9c7c8;
  }
  * { margin: 0; padding: 0; box-sizing: border-box; }
  html, body { width: 1200px; height: 1009px; overflow: hidden; }
  body {
    background: var(--backdrop);
    font-family: "Cinzel", serif;
    color: var(--ink);
    display: flex;
    flex-direction: column;
    align-items: center;
    justify-content: center;
    gap: 70px;
  }
  .card {
    position: relative;
    width: 700px;
    height: 400px;
    background: var(--card);
    border-radius: 26px;
    overflow: hidden;
    box-shadow: 0 4px 14px rgba(0,0,0,0.12);
  }
  .brand {
    display: flex;
    align-items: center;
    gap: 18px;
  }
  .brand-dot {
    width: 64px; height: 64px;
    border: 3px solid var(--ink);
    border-radius: 50%;
    flex: none;
  }
  .brand-name {
    font-size: 34px;
    font-weight: 400;
    letter-spacing: 1px;
    color: var(--ink);
    white-space: nowrap;
  }
  /* front */
  .card-front .brand { position: absolute; top: 48px; left: 150px; }
  .holder {
    position: absolute; top: 130px; left: 232px;
    font-size: 15px; letter-spacing: 1px; color: var(--ink-soft);
  }
  .address {
    position: absolute; top: 200px; left: 110px;
    font-size: 13px; line-height: 1.6; color: var(--ink-soft);
  }
  .contacts {
    position: absolute; top: 180px; left: 360px;
    list-style: none;
    font-size: 12px; line-height: 1.75; color: var(--ink-soft);
  }
  .contacts li { display: flex; align-items: center; gap: 8px; white-space: nowrap; }
  .contacts li::before {
    content: ""; width: 8px; height: 8px; background: var(--ink); flex: none;
  }
  .waves { position: absolute; left: 0; bottom: 0; width: 700px; height: 150px; }
  /* back */
  .card-back {
    display: flex; flex-direction: column; align-items: center; justify-content: center; gap: 36px;
  }
  .card-back .brand-dot { width: 80px; height: 80px; }
  .card-back .brand-name { font-size: 40px; }
  .web {
    font-size: 14px; letter-spacing: 4px; color: var(--ink-soft);
  }
</style>
</head>
<body>
  <section class="card card-front">
    <div class="brand">
      <span class="brand-dot"></span>
      <span class="brand-name">R &amp; T Auto Body</span>
    </div>
    <p class="holder">Delmor Quenivash</p>
    <p class="address">28476 Pellway Street<br>Corvale, CA 91890</p>
    <ul class="contacts">
      <li>T 818-555-0142</li>
      <li>F 818-555-0187</li>
      <li>C 818-555-0163</li>
      <li>rtautobodyinc@brivomail.com</li>
      <li>www.rtautobody-example.com</li>
    </ul>
    <svg class="waves" viewBox="0 0 700 150" preserveAspectRatio="none" aria-hidden="true">
      <path d="M0 40 C180 150 420 20 700 70 L700 150 L0 150 Z" fill="var(--band-light)"/>
      <path d="M0 58 C190 160 430 40 700 88 L700 150 L0 150 Z" fill="var(--band-mid)"/>
      <path d="M0 72 C200 168 440 60 700 104 L700 150 L0 150 Z" fill="var(--band-dark)"/>
    </svg>
  </section>

  <section class="card card-back">
    <div class="brand">
      <span class="brand-dot"></span>
      <span class="brand-name">R &amp; T Auto Body</span>
    </div>
    <p class="web">WWW.RTAUTOBODY-EXAMPLE.COM</p>
  </section>
</body>
</html>
```